Refer a Friend A5 Flyer for Healthcare Staff

We need an A5 flyer that we can hand out to existing and new staff members promoting our Refer a friend Scheme. We need the leaflet to encourage staff to talk to their family and friends about joining our Healthcare Agency, which provides staff to local care related establishments. Using our logo and brand colours blue and green, as per our website, the final design will need to clearly convey the benefits and attractions of referring additional staff to the team. In addition is the promotion of our SocialHub page, requesting staff to like the page and to like and share various posts.

Target Market(s)

Healthcare and potential Healthcare Staff

Industry/Entity Type

Healthcare

Colors
33b8a4
3277b5

Requirements
Must have
• Company Logo, Brand colours,
• text; "Refer a Friend and receive a £50 Bonus after just 1 completed shift"
• text; "3 easy steps to refer a friend, 1 Fill out your name on the back of your Business Card 2 Hand the card to your friend or any person you wish to refer, 3 ask your friend to present the card to us when they attend their interview"
• text; "Like and share any of our Open Days on SocialHub for a chance to win a prize, you can find us easily by searching @CarewellPlacementGroup"
• text; "Like our Page to stay up to date with our events and offers"
Nice to have
• care worker / elderly care / support worker pictures
• Content / pics from website www.carewellplacementgroup.co.uk

```html
<!DOCTYPE html>
<html lang="en">
<head>
<meta charset="utf-8">
<title>Refer a Friend – A5 Flyer</title>
<link href="https://fonts.googleapis.com/css2?family=Oswald:wght@300;400;500;600;700&display=swap" rel="stylesheet">
<style>
  :root {
    --page-bg: #d9d9d9;
    --brand-blue: #0a4df0;
    --brand-blue-deep: #0b3fd0;
    --step-blue: #3a8fe4;
    --step-number: #4aa2ee;
    --step-green: #4cef8e;
    --brand-teal: #33b8a4;
    --brand-mid: #3277b5;
    --footer-navy: #0e1f3b;
    --white: #ffffff;
    --logo-blue: #1f4fd8;
  }
  * { margin: 0; padding: 0; box-sizing: border-box; }
  html, body { width: 1200px; height: 1200px; overflow: hidden; }
  body {
    background: var(--page-bg);
    font-family: "Oswald", "Arial Narrow", sans-serif;
    color: var(--white);
    position: relative;
  }
  .flyer {
    position: absolute;
    left: 200px; top: 35px;
    width: 800px; height: 1130px;
    overflow: hidden;
    background: var(--footer-navy);
    box-shadow: 0 10px 30px rgba(0,0,0,.25);
  }
  /* Header band */
  .hero {
    position: absolute; left: 0; top: 0;
    width: 800px; height: 384px;
    background: var(--brand-blue);
  }
  .hero-photo {
    position: absolute; right: 0; top: 0;
    width: 330px; height: 384px;
    background: linear-gradient(90deg, rgba(10,77,240,0) 0%, rgba(60,140,200,.7) 35%, #6fae9a 60%, #9fcf8a 100%);
  }
  .hero-title {
    position: absolute; left: 56px; top: 110px;
    font-size: 104px; font-weight: 700; line-height: 1;
    letter-spacing: -1px;
  }
  .hero-offer {
    position: absolute; left: 56px; top: 220px;
    font-size: 44px; font-weight: 300; line-height: 42px;
    letter-spacing: -.5px;
  }
  /* Steps area */
  .care-photo {
    position: absolute; left: 0; top: 384px;
    width: 800px; height: 600px;
    background:
      radial-gradient(ellipse at 85% 25%, rgba(150,210,90,.85), rgba(150,210,90,0) 45%),
      radial-gradient(ellipse at 70% 70%, rgba(190,200,205,.55), rgba(190,200,205,0) 45%),
      linear-gradient(120deg, #2b3440 0%, #3c4a4f 40%, #5f7a62 70%, #7aa070 100%);
  }
  .steps {
    position: absolute; left: 56px; top: 520px;
    width: 430px;
  }
  .steps-heading {
    font-size: 32px; font-weight: 600; text-transform: uppercase;
    letter-spacing: 1px; line-height: 1; margin-bottom: 26px;
    white-space: nowrap;
  }
  .steps-heading .big { font-size: 46px; }
  .step {
    display: flex; height: 76px; margin-bottom: 7px;
    border: 2px solid var(--step-number);
  }
  .step-number {
    width: 74px; flex: none;
    background: var(--step-number);
    border-right: 2px solid #74b8f3;
    display: flex; align-items: center; justify-content: center;
    font-size: 50px; font-weight: 600;
  }
  .step-text {
    flex: 1;
    background: linear-gradient(90deg, var(--step-blue), var(--step-green));
    display: flex; align-items: center;
    padding: 0 18px;
    font-size: 23px; font-weight: 400; line-height: 23px;
  }
  /* Footer */
  .footer {
    position: absolute; left: 0; top: 981px;
    width: 800px; height: 149px;
    background: var(--footer-navy);
  }
  .social-line {
    position: absolute; left: 58px; top: 26px;
    display: flex; align-items: center; gap: 16px;
    font-size: 26px; font-weight: 500;
  }
  .social-dot {
    width: 32px; height: 32px; border-radius: 50%;
    background: var(--white);
  }
  .social-notes {
    position: absolute; left: 58px; top: 70px;
    display: flex; align-items: center; gap: 14px;
  }
  .share-badge {
    width: 36px; height: 36px; background: var(--step-blue);
  }
  .social-notes p {
    font-size: 16px; font-weight: 300; line-height: 23px;
  }
  .social-notes em { font-weight: 600; }
  .logo-panel {
    position: absolute; right: 0; top: 0;
    width: 253px; height: 149px;
  }
  .logo-panel svg { position: absolute; inset: 0; }
  .logo-name {
    position: absolute; right: 14px; top: 52px;
    width: 190px; text-align: center;
    font-size: 28px; font-weight: 400; line-height: 32px;
    color: var(--logo-blue);
  }
</style>
</head>
<body>
  <main class="flyer">
    <section class="hero">
      <div class="hero-photo" role="img" aria-label="Photo of a smiling care worker beside an elderly woman in a wheelchair"></div>
      <h1 class="hero-title">Refer a Friend</h1>
      <p class="hero-offer">and receive a £50 Bonus after just<br>1 completed shift</p>
    </section>

    <div class="care-photo" role="img" aria-label="Photo of a carer holding hands with a smiling elderly woman outdoors"></div>

    <section class="steps">
      <h2 class="steps-heading"><span class="big">3</span> Easy steps to refer a friend</h2>
      <div class="step">
        <div class="step-number">1</div>
        <div class="step-text">Fill out your name on the back of your Business Card</div>
      </div>
      <div class="step">
        <div class="step-number">2</div>
        <div class="step-text">Hand the card to your friend or any person you wish to refer</div>
      </div>
      <div class="step">
        <div class="step-number">3</div>
        <div class="step-text">Ask your friend to present the card to us when they attend their interview</div>
      </div>
    </section>

    <footer class="footer">
      <div class="social-line">
        <span class="social-dot"></span>
        <span>SocialHub.com/CarewellPlacementGroup</span>
      </div>
      <div class="social-notes">
        <span class="share-badge"></span>
        <p>Like and share any of our Open Days on SocialHub for a chance to <em>win a prize</em>.<br>Like our Page to stay up to date with our events and offers</p>
      </div>
      <div class="logo-panel">
        <svg width="253" height="149" viewBox="0 0 253 149">
          <polygon points="51,0 253,0 253,149 0,149" fill="#ffffff"/>
        </svg>
        <div class="logo-name">Carewell Placement</div>
      </div>
    </footer>
  </main>
</body>
</html>
```